TotPlanet Community Landing Page

TotPlanet is a virtual world built with childrens' needs in mind. It is an online portal where parents will find all kids' related stuffs and a community connect point for parents to interact and share their experiences.

We need the designs for 2 pages within TotPlanet:
- Landing Page for the Community Area
- Registration page for membership

1) The Landing Page need to have the following:

Logo & Main Background :- use the images attached

Page Title & Navigation Menu :-
The page title is "Community Connect"; navigation menu should be able to hold at least 6 tabs

Login Widget* :-
We want to put emphasis on the design of this.
For visitors, this is a normal login widget with username/password input fields, register button and 'login with chatterbook' button.
For logged-in users, this becomes a simple dashboard widget with Avatar, shortlinks and some useful navigation buttons.

"Groups" Section :-
This area holds an image, a short paragraph introducing "Groups", a widget showing 5-10 latest/popular groups and a 'Go to Groups' button at the bottom.

"Forum" Section :-
This area holds an image, a short paragraph introducing "Forum", a widget showing 5-10 latest/popular discussion topics and a 'Go to Forum' button at the bottom.

"Activities" Section -
This area holds an image, a short paragraph introducing "Forum", a widget showing 5-10 latest/popular events & activities and a 'Go to Activities' button at the bottom.

"Marketplace" Section :-
This area holds an image, a short paragraph introducing "Marketplace", a widget showing 5-10 latest/popular products and a 'Go to Marketplace' button at the bottom.

Social Media elements :-
The usual social media icons and chatterbook like box.

2) The Registration Page will need to contain the registration form as per the image attached.

Target Market(s)

Parents with kids ranging from 2 - 12 years old

Industry/Entity Type

Events

Requirements
Nice to have
• - colorful illustrations of kids or kids related images all around

```html
<!DOCTYPE html>
<html lang="en">
<head>
<meta charset="utf-8">
<title>TotPlanet – Community Connect</title>
<link rel="stylesheet" href="https://fonts.googleapis.com/css2?family=Short+Stack&family=Open+Sans:wght@400;700&display=swap">
<style>
  :root {
    --sky-top: #a9e6f5;
    --sky-mid: #3cc3ec;
    --cloud: #eef9fd;
    --grass-light: #a9cf3a;
    --grass-dark: #5b8d1a;
    --band-dark: #4b5a2b;
    --purple: #a31ee0;
    --purple-soft: #e7c7f2;
    --purple-pale: #f5e9fa;
    --text-dark: #2b2b2b;
    --btn-green-top: #a8c93a;
    --btn-green-bottom: #5d8a12;
    --btn-text: #8a17c8;
    --groups-title: #9b2ad8;
    --forum-title: #5aa82a;
    --activities-title: #e0771a;
    --market-title: #b0151c;
    --footer-top: #6f8f2c;
    --footer-bottom: #4d6b1e;
    --white: #ffffff;
  }
  * { box-sizing: border-box; margin: 0; padding: 0; }
  html, body { width: 1200px; height: 900px; overflow: hidden; background: var(--white); }
  body { font-family: "Open Sans", Arial, sans-serif; color: var(--text-dark); }
  .page { position: relative; width: 1200px; height: 900px; overflow: hidden; }

  /* Hero */
  .hero {
    position: absolute; left: 0; top: 0; width: 1200px; height: 455px;
    background:
      radial-gradient(ellipse 700px 120px at 650px 250px, var(--cloud) 0%, rgba(238,249,253,0) 70%),
      linear-gradient(180deg, var(--sky-top) 0%, var(--sky-mid) 22%, var(--cloud) 40%, #dff3fa 60%, var(--grass-light) 80%, var(--grass-dark) 100%);
  }
  .hero-band { position: absolute; left: 0; top: 455px; width: 1200px; height: 12px; background: var(--band-dark); }

  .brand {
    position: absolute; left: 170px; top: 40px;
    font-family: "Short Stack", cursive; font-size: 46px; color: var(--purple);
    display: flex; align-items: center; gap: 12px;
  }
  .brand-mark { width: 34px; height: 34px; border-radius: 50%; background: var(--purple); }

  .login-btn {
    position: absolute; left: 954px; top: 35px; width: 90px; height: 30px;
    border-radius: 4px; border: 1px solid #b66ad8;
    background: linear-gradient(180deg, #f0c8ff 0%, #c77be8 100%);
    font-family: Arial, sans-serif; font-size: 14px; color: #4a2a5a;
    display: flex; align-items: center; justify-content: center;
  }

  .network { position: absolute; left: 250px; top: 115px; width: 440px; height: 340px; }
  .bubble {
    position: absolute; border-radius: 50%; border: 3px solid;
  }

  .page-title {
    position: absolute; left: 660px; top: 128px; width: 380px;
    font-family: "Short Stack", cursive; font-size: 58px; line-height: 60px;
    color: var(--purple); text-align: center;
    text-shadow: 2px 3px 3px rgba(60,0,90,0.35);
  }
  .intro {
    position: absolute; left: 728px; top: 262px; width: 272px;
    font-size: 12px; font-weight: 700; line-height: 17.5px; text-align: justify;
  }

  /* Sections */
  .section { position: absolute; width: 420px; height: 165px; }
  .section-panel {
    position: absolute; left: 32px; top: 22px; width: 388px; height: 139px;
    border-radius: 6px;
    background: linear-gradient(180deg, var(--purple-soft) 0%, var(--purple-pale) 100%);
  }
  .section-photo {
    position: absolute; left: 0; top: 0; width: 192px; height: 137px;
    border-radius: 8px; box-shadow: 3px 4px 6px rgba(0,0,0,0.45);
  }
  .section-title {
    position: absolute; left: 207px; top: 0; font-family: "Short Stack", cursive;
    font-size: 29px; line-height: 38px; text-shadow: 1px 1px 1px rgba(0,0,0,0.25);
  }
  .section-text {
    position: absolute; left: 207px; top: 44px; width: 196px;
    font-size: 13px; line-height: 18px; text-align: justify;
  }
  .section-btn {
    position: absolute; top: 129px; height: 24px; padding: 0 12px; border-radius: 8px;
    background: linear-gradient(180deg, var(--btn-green-top) 0%, var(--btn-green-bottom) 100%);
    font-family: Arial, sans-serif; font-size: 12px; color: var(--btn-text);
    display: flex; align-items: center;
  }
  .groups { left: 173px; top: 476px; }
  .groups .section-photo { background: linear-gradient(135deg, #7ec3e0, #f3c88f 50%, #e58aa6); }
  .groups .section-title { color: var(--groups-title); }
  .groups .section-btn { left: 306px; }
  .forum { left: 614px; top: 476px; }
  .forum .section-panel { left: 23px; width: 388px; }
  .forum .section-photo { background: linear-gradient(135deg, #f3d6e2, #e8578f 50%, #d9d9d9); }
  .forum .section-title { left: 203px; color: var(--forum-title); }
  .forum .section-text { left: 201px; }
  .forum .section-btn { left: 298px; }
  .activities { left: 179px; top: 656px; }
  .activities .section-panel { left: 26px; top: 24px; height: 140px; }
  .activities .section-photo { height: 138px; background: linear-gradient(135deg, #f1f1f1, #f3c9a6 50%, #3c7fd0); }
  .activities .section-title { left: 206px; color: var(--activities-title); }
  .activities .section-text { left: 201px; }
  .activities .section-btn { left: 303px; top: 130px; }
  .marketplace { left: 614px; top: 656px; }
  .marketplace .section-panel { left: 23px; top: 24px; height: 140px; }
  .marketplace .section-photo { height: 138px; background: linear-gradient(135deg, #9bc0e4, #6a4b35 55%, #e7e0d2); }
  .marketplace .section-title { left: 203px; color: var(--market-title); }
  .marketplace .section-text { left: 201px; }
  .marketplace .section-btn { left: 294px; top: 130px; }

  /* Footer */
  .footer {
    position: absolute; left: 0; top: 836px; width: 1200px; height: 64px;
    background: linear-gradient(180deg, var(--footer-top) 0%, var(--footer-bottom) 100%);
    color: var(--white); font-size: 19px;
  }
  .follow { position: absolute; left: 422px; top: 18px; font-size: 22px; }
  .social { position: absolute; top: 14px; display: flex; align-items: center; gap: 6px; }
  .social-square { width: 36px; height: 36px; background: var(--white); border-radius: 3px; }
  .social-circle { width: 32px; height: 32px; background: var(--white); border-radius: 50%; }
  .social-chatterbook { left: 556px; }
  .social-subscribe { left: 730px; }
  .social-chirper { left: 904px; }
</style>
</head>
<body>
<main class="page">
  <header class="hero" role="img" aria-label="Sunny sky with rainbow, clouds, green hills and butterflies"></header>
  <div class="hero-band"></div>

  <div class="brand"><span class="brand-mark"></span>TotPlanet</div>
  <div class="login-btn">Log In</div>

  <svg class="network" viewBox="0 0 440 340" aria-hidden="true">
    <g fill="none" stroke="#333" stroke-width="3" stroke-dasharray="8 7">
      <path d="M120 50 C 60 70, 60 120, 70 150"/>
      <path d="M245 40 C 330 20, 370 60, 355 110"/>
      <path d="M80 200 C 10 240, 30 300, 90 290"/>
      <path d="M150 140 C 180 110, 230 120, 260 140"/>
      <path d="M350 200 C 350 250, 310 290, 290 300"/>
      <path d="M210 330 C 240 320, 250 300, 270 290"/>
      <path d="M230 230 C 240 260, 250 270, 250 275"/>
    </g>
  </svg>
  <div class="bubble" role="img" aria-label="Photo of a smiling boy" style="left:390px;top:118px;width:135px;height:108px;border-color:#e2b214;background:#f3d7bf;"></div>
  <div class="bubble" role="img" aria-label="Photo of a girl in a blue hat" style="left:268px;top:213px;width:118px;height:108px;border-color:#2b5a8a;background:#5a6e7c;"></div>
  <div class="bubble" role="img" aria-label="Photo of a girl in a wide hat" style="left:398px;top:243px;width:132px;height:105px;border-color:#8a1fc8;background:#5d86b0;"></div>
  <div class="bubble" role="img" aria-label="Photo of a dark-haired boy" style="left:548px;top:208px;width:135px;height:107px;border-color:#c0578a;background:#8a6a58;"></div>
  <div class="bubble" role="img" aria-label="Photo of a girl with a red bow" style="left:325px;top:340px;width:135px;height:110px;border-color:#d9261c;background:#e8c6b3;"></div>
  <div class="bubble" role="img" aria-label="Photo of a curly-haired boy" style="left:500px;top:343px;width:135px;height:108px;border-color:#1c3fa8;background:#3a3a4a;"></div>

  <h1 class="page-title">Community Connect</h1>
  <p class="intro">“Lorem ipsum dolor sit amet, consectetuer adipiscing elit, sed diam nonummy nibh euismod tincidunt ut laoreet dolore magna. aliquam erat volutpat. Ut wisi enim ad minim veniam, quis nostrud exerci tation”</p>

  <section class="section groups">
    <div class="section-panel"></div>
    <div class="section-photo" role="img" aria-label="Photo of a group of smiling children"></div>
    <h2 class="section-title">Groups</h2>
    <p class="section-text">Lorem ipsum dolor sit amet, consectetuer adipiscing elit, sed diam nonummy nibh euismod tincidunt ut laoreet dolore</p>
    <span class="section-btn">Go to Groups</span>
  </section>

  <section class="section forum">
    <div class="section-panel"></div>
    <div class="section-photo" role="img" aria-label="Photo of children gathered around a laptop"></div>
    <h2 class="section-title">Forum</h2>
    <p class="section-text">Lorem ipsum dolor sit amet, consectetuer adipiscing elit, sed diam nonummy nibh euismod tincidunt ut laoreet dolore</p>
    <span class="section-btn">Go to Forum</span>
  </section>

  <section class="section activities">
    <div class="section-panel"></div>
    <div class="section-photo" role="img" aria-label="Photo of a boy with painted face and hands"></div>
    <h2 class="section-title">Activities</h2>
    <p class="section-text">Lorem ipsum dolor sit amet, consectetuer adipiscing elit, sed diam nonummy nibh euismod tincidunt ut laoreet dolore</p>
    <span class="section-btn">Go to Activities</span>
  </section>

  <section class="section marketplace">
    <div class="section-panel"></div>
    <div class="section-photo" role="img" aria-label="Photo of a nursery room with a crib"></div>
    <h2 class="section-title">Marketplace</h2>
    <p class="section-text">Lorem ipsum dolor sit amet, consectetuer adipiscing elit, sed diam nonummy nibh euismod tincidunt ut laoreet dolore</p>
    <span class="section-btn">Go to Marketplace</span>
  </section>

  <footer class="footer">
    <span class="follow">Follow us</span>
    <span class="social social-chatterbook"><span class="social-square"></span>chatterbook</span>
    <span class="social social-subscribe">
      <svg width="40" height="26" viewBox="0 0 40 26" aria-hidden="true">
        <rect x="1" y="1" width="38" height="24" fill="none" stroke="#fff" stroke-width="2"/>
        <path d="M1 1 L20 15 L39 1 M1 25 L15 12 M39 25 L25 12" fill="none" stroke="#fff" stroke-width="2"/>
      </svg>Subscribe</span>
    <span class="social social-chirper"><span class="social-circle"></span>Chirper</span>
  </footer>
</main>
</body>
</html>
```